Billboard for personal injury chiropractors office

We are a personal injury chiropractor clinic.
I need a Billboard with the company name as the dominating factor. Also a smaller picture or 2 of something creative, like a car accident or an arm in a cast off to the sides.
We Like something Clean and Simple and Eye Catching. Please make the picture Small and Off To The Side. The MAIN FOCUS areas are the… name Varden Chiropractic Clinic
At the top CAR ACCIDENT INJURY?
AND at the bottom our number 418-27-FLEXA.
Dr.Milo R. Varden in bold somewhere with the word chiropractor under the doctors name in a text.

Im open to red lettering on white backgrounds, red on yellow backgrounds and I'm also open to reds blues white and yellow. I'd prefer yellow if used be across the bottom.

I am uploading a very rough draft of what we are after along with a screenshot of the tv commercial showing the yellow

DO NOT USE THE LOGO ON THE COMMERCIAL. I JUST WANT THE NAME TYPED LIKE ON SAMPLE BILLBOARD.

Industry/Entity Type

Chiropractic

Colors
0054AA
0677BA
7BADD7
CADEEF
E8F1F8
FFF300
FFF600
FEFA6F
FFFEC7
FFFEE8
EB3D1F
EC4F4E
F09395
F8D3D4
FCEDEE

Requirements
Must have
• Eye catching ,bold

```html
<!DOCTYPE html>
<html lang="en">
<head>
<meta charset="utf-8">
<title>Varden Chiropractic Clinic – Billboard</title>
<link rel="stylesheet" href="https://fonts.googleapis.com/css2?family=Bebas+Neue&family=Poppins:wght@600;700&display=swap">
<style>
  :root {
    --stage: #000000;
    --board-yellow: #FFFA00;
    --tab-red: #C00000;
    --ink: #0A0A0A;
    --paper: #FFFFFF;
    --photo-light: #F4F0B0;
    --photo-mid: #B9BCC4;
    --photo-dark: #8E939C;
  }
  html, body {
    margin: 0;
    padding: 0;
    width: 1200px;
    height: 1200px;
    overflow: hidden;
    background: var(--stage);
  }
  .canvas {
    display: block;
    width: 1200px;
    height: 1200px;
  }
  .board-bg { fill: var(--board-yellow); }
  .tab { fill: var(--tab-red); }
  .headline {
    font-family: 'Bebas Neue', sans-serif;
    fill: var(--paper);
    font-size: 66px;
  }
  .clinic-name {
    font-family: 'Bebas Neue', sans-serif;
    fill: var(--ink);
    font-size: 68px;
    stroke: var(--ink);
    stroke-width: 1.5px;
  }
  .divider { stroke: var(--ink); stroke-width: 2; }
  .doctor-name {
    font-family: 'Poppins', sans-serif;
    font-weight: 600;
    fill: var(--ink);
    font-size: 42px;
  }
  .call-label {
    font-family: 'Poppins', sans-serif;
    font-weight: 600;
    fill: var(--paper);
    font-size: 29px;
  }
  .phone-number {
    font-family: 'Poppins', sans-serif;
    font-weight: 700;
    fill: var(--paper);
    font-size: 50px;
  }
  .base-strip { fill: var(--stage); }
</style>
</head>
<body>
<svg class="canvas" viewBox="0 0 1200 1200" xmlns="http://www.w3.org/2000/svg">
  <defs>
    <linearGradient id="photoFade" x1="0" y1="0" x2="1" y2="0">
      <stop offset="0" stop-color="#FFFA00" stop-opacity="0"/>
      <stop offset="0.2" stop-color="#E8C84A"/>
      <stop offset="0.45" stop-color="#C9CCD2"/>
      <stop offset="1" stop-color="#9A9FA8"/>
    </linearGradient>
  </defs>

  <g class="billboard">
    <rect class="board-bg" x="99" y="400" width="1002" height="291"/>

    <rect class="photo" x="700" y="400" width="401" height="291" fill="url(#photoFade)"
          role="img" aria-label="Photo of a crashed red car and a man in a grey T-shirt holding his arm in a white cast"/>
    <rect class="base-strip" x="692" y="674" width="409" height="17"/>

    <path class="tab headline-tab" d="M130 400 H692 V462 Q692 487 667 487 H155 Q130 487 130 462 Z"/>
    <text class="headline" x="411" y="472" text-anchor="middle" textLength="486" lengthAdjust="spacingAndGlyphs">CAR ACCIDENT INJURY?</text>

    <text class="clinic-name" x="411" y="553" text-anchor="middle" textLength="522" lengthAdjust="spacingAndGlyphs">VARDEN CHIROPRACTIC CLINIC</text>
    <line class="divider" x1="150" y1="573" x2="674" y2="573"/>

    <text class="doctor-name" x="411" y="621" text-anchor="middle" textLength="412" lengthAdjust="spacingAndGlyphs">Dr.Milo R. Varden</text>

    <path class="tab call-tab" d="M130 691 V658 Q130 633 155 633 H667 Q692 633 692 658 V691 Z"/>
    <text class="call-label" x="160" y="678" textLength="142" lengthAdjust="spacingAndGlyphs">Call Now</text>
    <text class="phone-number" x="314" y="678" textLength="344" lengthAdjust="spacingAndGlyphs">418-555-0193</text>
  </g>
</svg>
</body>
</html>
```